RollUp Druck 85x200cm für Finanzdienstleister
Zielgruppe
Die kwa Stock GmbH stellt unter ihrer Marke "Hausfond-Lotse" Baufinanzierungsberatern professionelle Lösungen zur Finanzierungsabwicklung zur Verfügung. Nähere Informationen rund um das Unternehmen erhalten Sie unter www.hausfond-lotse.de.
Aufgabenstellung
Als ergänzende Marketingmaßnahme ist die Anschaffung von RollUps geplant. Für diese wünschen wir uns ein thematisch zur Kundenkommunikation passendes RollUp mit den obigen Maßen und den Werbeslogan "Baufinanzierung - seriöse Beratung und beste Konditionen aus über 100 Banken". Die Grafik soll sich an den branchenüblichen Motiven orientieren, aber auch für frische Ideen sind wir offen.
Alle mit 5 Sterne bewerteten Entwürfe werden wir von den entsprechenden Designer zum angebotenen Preis kaufen (sprich 4 Entwürfe mit 5 Sternen = 5x Preisgeld).

```html
<!DOCTYPE html>
<html lang="de">
<head>
<meta charset="utf-8">
<title>Hausfond-Lotse – RollUp Baufinanzierung</title>
<link rel="stylesheet" href="https://fonts.googleapis.com/css2?family=Open+Sans:wght@400;600;700&family=Arimo:wght@400;700&display=swap">
<style>
  :root {
    --stage: #eeeff1;
    --paper: #ffffff;
    --brand-blue: #1766b3;
    --text-blue: #1a5ea8;
    --band-top: #dce9f5;
    --band-mid: #9fc4e2;
    --band-low: #b9d5ec;
    --photo-top: #cddfee;
    --photo-bottom: #e6edf3;
  }
  * { margin: 0; padding: 0; box-sizing: border-box; }
  html, body { width: 1017px; height: 1200px; overflow: hidden; background: var(--stage); }
  .rollup {
    position: absolute; left: 253px; top: 0;
    width: 510px; height: 1200px;
    background: var(--paper); overflow: hidden;
    font-family: "Open Sans", sans-serif;
  }
  .header {
    position: absolute; left: 0; top: 0; width: 100%; height: 215px;
    background: linear-gradient(#ffffff 40%, #e6eff8);
  }
  .brand {
    position: absolute; left: 70px; top: 82px;
    display: flex; align-items: center; gap: 18px;
  }
  .brand-mark { width: 44px; height: 44px; background: var(--brand-blue); }
  .brand-name { font-size: 40px; font-weight: 700; color: var(--brand-blue); letter-spacing: 0.5px; }
  .header-curve { position: absolute; left: 0; top: 170px; width: 510px; height: 60px; }
  .headline {
    position: absolute; left: 0; top: 212px; width: 100%;
    text-align: center; font-size: 56px; font-weight: 400;
    color: var(--brand-blue); letter-spacing: 1px;
  }
  .band {
    position: absolute; left: 0; top: 285px; width: 100%; height: 700px;
    background: linear-gradient(var(--band-top), var(--band-mid) 25%, var(--band-mid) 55%, var(--band-low) 80%, #e8f0f8);
    border-radius: 50% 50% 0 0 / 30px 30px 0 0;
  }
  .slogan {
    position: absolute; background: var(--paper); color: var(--brand-blue);
    font-size: 37px; line-height: 48px; padding: 0 12px; border-radius: 10px;
    white-space: nowrap;
  }
  .slogan--one { right: 12px; top: 335px; }
  .slogan--two { left: 6px; top: 397px; }
  .slogan--three { right: 12px; top: 462px; }
  .benefits {
    position: absolute; left: 0; top: 522px; width: 100%;
    list-style: none; text-align: center;
    font-family: "Arimo", sans-serif; font-size: 16px; font-weight: 700; color: var(--text-blue);
  }
  .benefits li { height: 37.5px; line-height: 22px; }
  .photo {
    position: absolute; left: 0; top: 955px; width: 510px; height: 225px;
    background: linear-gradient(180deg, var(--photo-top), var(--photo-bottom));
  }
</style>
</head>
<body>
  <main class="rollup">
    <header class="header">
      <div class="brand">
        <span class="brand-mark"></span>
        <span class="brand-name">Hausfond-Lotse</span>
      </div>
    </header>
    <svg class="header-curve" viewBox="0 0 510 60" aria-hidden="true">
      <path d="M0 35 Q255 -5 510 35 L510 60 L0 60 Z" fill="#ffffff"/>
    </svg>
    <h1 class="headline">Baufinanzierung</h1>
    <div class="band"></div>
    <p class="slogan slogan--one">seriöse Beratung</p>
    <p class="slogan slogan--two">und beste Konditionen</p>
    <p class="slogan slogan--three">aus über 100 Banken</p>
    <ul class="benefits">
      <li>über 100 Banken im Vergleich</li>
      <li>wir vergleichen die günstigsten Angebote für Sie</li>
      <li>persönliche Beratung vor Ort</li>
      <li>zertifizierter Berater</li>
      <li>kostenlose &amp; unverbindliche Beratung</li>
      <li>Fördermittelberatung zur Finanzierung</li>
      <li>Finanzierungsbegleitung bis zum Einzug</li>
      <li>langjährige Erfahrung in der Baufinanzierung</li>
      <li>Zuverlässigkeit, weil es um Ihr Geld geht</li>
    </ul>
    <div class="photo" role="img" aria-label="Foto: Handschlag zweier Geschäftsleute in dunklen Anzügen vor hellem Hintergrund"></div>
  </main>
</body>
</html>
```